Business Card Design

We need a new business card for our restaurant/motel as we are new owners. Our business is in a small community in a rainforest north of Townsville, Queensland AUSTRALIA and we are on a mountain 3000 feet above sea level. Visitors come here to see the wide variety of birds (This area is especially noted for the cassowary and riflebird), travel the many bush walks and enjoy the cooler climate. We would like you to use as the main colours blue and green - the buildings are painted in those colours and reflect the green for the forest and blue for the rain/sky. Yellow could also be used. The card should be bright and cheerful.
Travel
Ferncrest Lodge Yarrondi
Licensed Café/ Restaurant & Motel
14 Coralwood Lane KELBRIDGE Qld 4823
Ph: 07 4391 2574 Fax: 07 43916420
reception@ferncrestlodgeyarrondi.example
www.ferncrestlodgeyarrondi.example
like us on Chatterbook

```html
<!DOCTYPE html>
<html lang="en">
<head>
<meta charset="utf-8">
<title>Ferncrest Lodge Yarrondi – Business Card</title>
<link rel="stylesheet" href="https://fonts.googleapis.com/css2?family=Berkshire+Swash&family=Tinos:ital,wght@0,400;1,700&family=Arimo:wght@700&display=swap">
<style>
  :root {
    --stage: #eceeef;
    --leaf: #c4e47c;
    --leaf-light: #d9efa6;
    --paper: #ffffff;
    --sky: #1f6db7;
    --deep: #1a56a8;
    --sun: #f3e21a;
    --ink: #222222;
  }
  * { margin: 0; padding: 0; box-sizing: border-box; }
  html, body { width: 1200px; height: 868px; overflow: hidden; background: var(--stage); }
  .canvas { position: relative; width: 1200px; height: 868px; }
  .card {
    position: absolute; left: 109px; top: 139px; width: 1020px; height: 573px;
    border-radius: 8px 130px 8px 140px;
    background: linear-gradient(135deg, var(--leaf-light) 0%, var(--leaf) 45%, var(--leaf) 100%);
    overflow: hidden;
    box-shadow: 0 8px 18px rgba(0,0,0,0.18);
  }
  .card__panel { position: absolute; inset: 0; width: 1020px; height: 573px; }
  .brand-name {
    position: absolute; left: 47px; top: 62px;
    font-family: "Berkshire Swash", cursive; font-size: 40px; color: var(--sky);
    white-space: nowrap;
  }
  .tagline {
    position: absolute; left: 61px; top: 131px;
    font-family: "Tinos", serif; font-style: italic; font-weight: 700;
    font-size: 24px; color: var(--ink);
  }
  .contacts { position: absolute; left: 68px; top: 193px; list-style: none; }
  .contacts li {
    display: flex; align-items: center; height: 46px;
    font-family: "Tinos", serif; font-size: 26px; color: var(--ink);
  }
  .contacts svg { width: 26px; height: 26px; margin-right: 16px; flex: none; }
  .birds {
    position: absolute; left: 96px; top: 413px; width: 377px; height: 129px;
    border-radius: 20px;
    background: radial-gradient(ellipse at center, rgba(31,109,183,0.45), rgba(31,109,183,0.08) 75%);
  }
  .social {
    position: absolute; left: 508px; top: 476px;
    display: flex; align-items: center; gap: 10px;
    font-family: "Arimo", sans-serif; font-weight: 700; font-size: 22px; color: var(--ink);
  }
  .social__mark { width: 30px; height: 30px; background: var(--deep); border-radius: 4px; }
  .social__name { color: var(--deep); }
  .logo-name {
    position: absolute; left: 640px; top: 120px; width: 340px;
    text-align: center;
    font-family: "Tinos", serif; font-weight: 400; font-size: 44px; line-height: 1.05;
    color: var(--sky);
  }
</style>
</head>
<body>
<main class="canvas">
  <section class="card">
    <svg class="card__panel" viewBox="0 0 1020 573" aria-hidden="true">
      <path d="M571 0 H1020 V300 C1000 330 900 345 842 382 C700 330 560 200 571 0 Z" fill="var(--paper)"/>
      <path d="M560 0 C548 205 690 335 842 382" fill="none" stroke="var(--sun)" stroke-width="8"/>
      <path d="M571 0 C560 200 700 330 842 382" fill="none" stroke="var(--deep)" stroke-width="7"/>
    </svg>

    <h1 class="brand-name">Ferncrest Lodge Yarrondi</h1>
    <p class="tagline">Licensed Café/ Restaurant &amp; Motel</p>

    <ul class="contacts">
      <li>
        <svg viewBox="0 0 24 24"><path d="M6 3l4 1 1 5-3 2c1 3 3 5 6 6l2-3 5 1 1 4c-1 2-3 3-5 3C9 21 3 15 3 7c0-2 1-4 3-4z" fill="var(--sky)"/></svg>
        07 4391 2574
      </li>
      <li>
        <svg viewBox="0 0 24 24"><rect x="6" y="3" width="12" height="7" fill="none" stroke="var(--sky)" stroke-width="2"/><rect x="3" y="10" width="18" height="9" rx="2" fill="var(--sky)"/><rect x="7" y="15" width="10" height="6" fill="#fff" stroke="var(--sky)" stroke-width="1.5"/></svg>
        07 43916420
      </li>
      <li>
        <svg viewBox="0 0 24 24"><rect x="3" y="6" width="18" height="13" fill="none" stroke="var(--sky)" stroke-width="2"/><path d="M3 6l9 7 9-7" fill="none" stroke="var(--sky)" stroke-width="2"/></svg>
        reception@ferncrestlodgeyarrondi.example
      </li>
      <li>
        <svg viewBox="0 0 24 24"><circle cx="12" cy="12" r="9" fill="none" stroke="var(--sky)" stroke-width="2"/><ellipse cx="12" cy="12" rx="4" ry="9" fill="none" stroke="var(--sky)" stroke-width="1.5"/><path d="M3 12h18M5 7h14M5 17h14" stroke="var(--sky)" stroke-width="1.5"/></svg>
        www.ferncrestlodgeyarrondi.example
      </li>
      <li>
        <svg viewBox="0 0 24 24"><path d="M2 11l10-8 10 8h-3v10H5V11z" fill="var(--sky)"/><rect x="10" y="14" width="4" height="7" fill="#fff"/></svg>
        14 Coralwood Lane KELBRIDGE Qld 4823
      </li>
    </ul>

    <div class="birds" role="img" aria-label="Flock of blue bird silhouettes in flight"></div>

    <p class="social">Like us on <span class="social__mark"></span><span class="social__name">Chatterbook</span></p>

    <p class="logo-name">Ferncrest Lodge Yarrondi</p>
  </section>
</main>
</body>
</html>
```